Executive Summary

Create a one page executive summary of a venture fund - with the information here:
https://files.brindlepath.net/doc/7qR2mXvT9kLp4sWn8yZcB3fHj6dKa5eU/view?share=open

```html
<!DOCTYPE html>
<html lang="en">
<head>
<meta charset="utf-8">
<title>Meridian Decarbonization Partnership Fund — Executive Summary</title>
<link rel="stylesheet" href="https://fonts.googleapis.com/css2?family=Jost:wght@400;500;600;700&display=swap">
<style>
:root{
  --navy:#13284f;
  --red:#ec3f36;
  --purple:#7a2590;
  --cyan:#0ea3e0;
  --ink:#1b1b1b;
  --muted:#4a4a4a;
  --paper:#ffffff;
  --stage:#9a9a9a;
}
*{box-sizing:border-box;margin:0;padding:0}
html,body{width:1200px;height:1200px;overflow:hidden;background:var(--stage);font-family:"Jost",sans-serif;color:var(--ink)}
.sheet{position:absolute;left:514px;top:90px;width:172px;height:1019px;background:var(--paper);display:flex;flex-direction:column;overflow:hidden}
.sheet > *{flex:none;overflow:hidden}
.h2{font-weight:700;font-size:10px;line-height:1.2;text-align:center}

.band-header{height:72px;background:var(--navy);color:#fff;display:flex;align-items:center;justify-content:center;text-align:center;font-weight:600;font-size:10.5px;line-height:1.35;padding:0 10px}

.intro{height:110px;padding:12px 10px 0;text-align:center}
.intro .tag{font-size:5.4px}
.intro .sub{font-size:3.4px;color:var(--muted);margin-top:6px}
.intro .h2{margin-top:5px;font-size:11px}
.intro .lede{font-size:3.4px;color:var(--muted);margin-top:1px}
.thesis-list{text-align:left;margin-top:5px;padding-left:8px}
.thesis-list dt{font-size:3.6px;font-weight:600;margin-top:4px}
.thesis-list dd{font-size:3.3px;color:var(--muted);line-height:1.35}

.focus{height:53px;padding:6px 10px 0;text-align:center}
.focus p{font-size:3.3px;line-height:1.4;color:var(--muted);margin-top:3px}

.team{height:141px;background:var(--red);color:#fff;padding:5px 8px 0}
.team .h2{color:#fff;margin-bottom:4px}
.member{display:flex;align-items:center;gap:4px;height:20px}
.member.right{flex-direction:row-reverse}
.member .frame{flex:none;width:15px;height:15px;border:0.6px solid #fff}
.member .bio{flex:1;text-align:center;font-size:3px;line-height:1.35}
.member .bio b{display:block;font-size:3.4px;font-weight:600}

.investors{height:139px;padding-top:6px}
.investors .h2{margin-bottom:5px}
.grid{display:grid;grid-template-columns:1fr 1fr;gap:4px;padding:0 6px}
.card{height:51px;padding:4px;color:#fff;text-align:left;font-size:3.1px;line-height:1.4;overflow:hidden}
.card b{display:block;font-size:3.5px;font-weight:600;margin-bottom:2px}
.card i{font-style:normal;font-weight:600}
.card.purple{background:var(--purple)}
.card.cyan{background:var(--cyan)}

.terms{height:71px;padding-top:3px}
.terms ul{list-style:none;text-align:left;font-size:3.3px;line-height:1.5;color:var(--muted);padding:3px 0 0 26px}

.track-wrap{height:105px;padding:3px 6px 0}
.track{border:0.7px solid #888;border-radius:5px;height:98px;padding:3px 4px 0;overflow:hidden}
.track .h2{margin-bottom:2px}
.track table{width:100%;border-collapse:collapse;font-size:3.1px;text-align:left}
.track th{font-weight:600;padding:2px;vertical-align:top;height:13px;line-height:1.3}
.track td{padding:2px;height:13px;vertical-align:middle}
.track .mid{background:var(--red);color:#fff}

.fund1{height:54px;padding:8px 8px 0;text-align:left}
.fund1 .h3{font-weight:700;font-size:5.6px}
.fund1 ul{list-style:none;font-size:3.2px;line-height:1.45;color:var(--muted);padding:3px 0 0 30px}

.portfolio{height:230px;padding:6px 7px 4px;display:flex;flex-direction:column}
.portfolio .h2{margin-bottom:3px}
.portfolio .blocks{flex:1;display:flex;flex-direction:column;justify-content:space-between}
.portfolio p{font-size:3.2px;line-height:1.4;color:var(--muted);margin-bottom:2px;text-align:left}
.portfolio p.lead{color:var(--ink);font-weight:600;font-size:3.5px;margin-bottom:1px}
.portfolio p.quote b{color:var(--ink);font-weight:600}

.join{height:44px;background:var(--red);color:#fff;text-align:center;padding-top:5px}
.join .h2{color:#fff;margin-bottom:2px}
.join p{font-size:3.2px;line-height:1.35}
.join .link{font-size:2.6px;word-break:break-all;padding:0 8px}
</style>
</head>
<body>
<main class="sheet">
  <header class="band-header">Meridian Decarbonization<br>Partnership&nbsp;&nbsp;Fund</header>

  <section class="intro">
    <p class="tag">Designed for Corporate Decarbonization</p>
    <p class="sub">Partnerships Powered by Meridian Capital</p>
    <h2 class="h2">Thesis</h2>
    <p class="lede">Investing in Early Stage Decarbonization Startups alongside</p>
    <dl class="thesis-list">
      <dt>Collaboration</dt><dd>Corporate LPs partner on collaborative pilots, insights, co-investment and more</dd>
      <dt>Party</dt><dd>Shared alignment of Meridian on strategic and financial returns</dd>
      <dt>Impact</dt><dd>10 GT CO2e reduction potential per portfolio company by 2050</dd>
    </dl>
  </section>

  <section class="focus">
    <h2 class="h2">Investment Focus</h2>
    <p>We invest in frontier decarbonization technologies that accelerate venture returns and strategic value for corporates, such as AI &amp; Robotics • Energy Efficiency • Next-Gen Materials • Clean Energy Infrastructure • Carbon Management • Sustainable Food • Circular Systems • Grid Integration</p>
  </section>

  <section class="team">
    <h2 class="h2">Team</h2>
    <div class="member"><span class="frame"></span><p class="bio"><b>Aria Lindqvist, Managing Partner (California)</b>Climate venture investor and former operator scaling clean-tech startups</p></div>
    <div class="member right"><span class="frame"></span><p class="bio"><b>Tomas Revell, PhD, Venture Partner (Texas)</b>Former chemical engineer, clean-tech founder and board advisor</p></div>
    <div class="member"><span class="frame"></span><p class="bio"><b>Priya Namdar, PhD, Venture Partner (New York)</b>Materials scientist and venture builder in energy systems</p></div>
    <div class="member right"><span class="frame"></span><p class="bio"><b>Lena Okafor, CFA, Vice President (California)</b>Former investment banker, diligence and portfolio support</p></div>
    <div class="member"><span class="frame"></span><p class="bio"><b>Colette Marsh, Chief of Staff (California)</b>Operations and investor relations for growth-stage startups</p></div>
    <div class="member right"><span class="frame"></span><p class="bio"><b>Jonas Ferreira, LP, Impact Advisor (New York)</b>Climate policy and sustainability strategy advisor</p></div>
  </section>

  <section class="investors">
    <h2 class="h2">Design for Strategic Investors</h2>
    <div class="grid">
      <div class="card purple"><b>Deal Flow Access</b><i>Weekly Deal Reviews</i><br>Early access to curated startup pipeline<br><i>Startup Pipeline</i><br>Shared CRM for sourcing</div>
      <div class="card cyan"><b>Sector Intelligence</b><i>Research Reports</i><br>Quarterly deep dives on emerging tech<br><i>Knowledge Exchange</i><br>Workshops with founders and experts</div>
      <div class="card cyan"><b>Advanced Involvement</b><i>Co-Investment Rights</i><br>Pro rata alongside the fund<br><i>Due Diligence Support</i><br>Shared technical review</div>
      <div class="card purple"><b>Tailored Engagement</b><i>Custom Deal Sourcing</i><br>Thematic searches for LP needs<br><i>Pilot Programs</i><br>Direct paths to strategic partners</div>
    </div>
  </section>

  <section class="terms">
    <h2 class="h2">Fund Term Overview</h2>
    <ul>
      <li>• Fund Size: $50M</li>
      <li>• Term: 10+1+1 Years</li>
      <li>• Stage Focus: Seed and Series A</li>
      <li>• Target Returns: 3x net multiple, 25% IRR</li>
      <li>• Check Size: $0.5M–$2M initial investments</li>
      <li>• Follow-on Reserve: 50%</li>
      <li>• Geography: North America</li>
      <li>• Management Fee: 2%, Carry: 20%</li>
    </ul>
  </section>

  <div class="track-wrap">
    <section class="track">
      <h2 class="h2">Track Record</h2>
      <table>
        <thead><tr><th>Company Position<br>Seed Round</th><th class="mid">Stage Invested</th><th>Current Stage</th></tr></thead>
        <tbody>
          <tr><td>Halcyra</td><td class="mid">Series A Bridge 2019</td><td>Series C 2023</td></tr>
          <tr><td>Solvane Labs</td><td class="mid">Seed 2018</td><td>Growth Stage 2024</td></tr>
          <tr><td>Kestrel Materials</td><td class="mid">Seed 2020</td><td>Series B 2023</td></tr>
          <tr><td>Tidewell Infrastructure</td><td class="mid">Seed Extension 2021</td><td>Series B 2024</td></tr>
          <tr><td>Northbay Bio</td><td class="mid">Pre-Seed 2019</td><td>Series A 2022</td></tr>
        </tbody>
      </table>
    </section>
  </div>

  <section class="fund1">
    <h3 class="h3">Fund I Investments so far (continue to invest)</h3>
    <ul>
      <li>Quarrel Grain, Seed, Series A</li>
      <li>Fernline Foods, Seed</li>
      <li>Velora Fibers, Seed</li>
      <li>Ashgrove Power, Pre-Seed</li>
      <li>Brightcoil, Seed</li>
    </ul>
  </section>

  <section class="portfolio">
    <h2 class="h2">Example Portfolio Startups</h2>
    <div class="blocks">
      <div class="block">
        <p class="lead">Quarrel Grain: low-emission grain production</p>
        <p>Quarrel Grain has developed a proprietary process that lowers methane emissions from rice paddies while improving yields, giving farmers a clear economic reason to switch practices. The team works directly with growers and buyers, and its field trials across three regions show strong reductions in water use and fertilizer demand, opening new carbon markets for the whole supply chain.</p>
        <p class="quote">“Meridian has been a true partner from our first pilots, connecting us with corporate buyers early and helping us shape our go-to-market plan.” <b>Co-Founder, Quarrel Grain</b></p>
      </div>
      <div class="block">
        <p class="lead">Fernline Foods: plant protein at price parity</p>
        <p>Fernline produces whole-cut plant proteins that match conventional meat on taste and cost, using a fermentation platform that scales with existing food manufacturing lines. Its products are now in food service trials and the company is expanding capacity with two regional partners.</p>
        <p class="quote">“The introductions to strategic LPs accelerated our path to retail shelves, and the team’s diligence sharpened our plan.” <b>CEO, Fernline Foods</b></p>
      </div>
      <div class="block">
        <p class="lead">Velora Fibers: low-carbon textile fibers</p>
        <p>Velora turns agricultural waste into high-quality textile fibers that replace synthetics, cutting emissions and water use while supplying apparel brands with a traceable, durable material at competitive cost. After a successful pilot line, the company is preparing its first commercial plant and signing offtake agreements with global brands.</p>
        <p class="quote">“Meridian helped us structure pilots with two global brands and brought deep technical diligence to the table when we needed it most.” <b>Co-Founder, Velora Fibers</b></p>
      </div>
    </div>
  </section>

  <footer class="join">
    <h2 class="h2">Join Us</h2>
    <p>For any inquiries please contact:</p>
    <p>Aria Lindqvist, Managing Partner</p>
    <p class="link">https://files.brindlepath.net/doc/7qR2mXvT9kLp4sWn8yZcB3fHj6dKa5eU/view?share=open</p>
  </footer>
</main>
</body>
</html>
```